Business Stationery for Bramwell Oakes Recruitment Ltd
Marnie Thwaite
Cutting-Edge
Director
42 Quillmere Road
Teddington
Middlesex
KT4 9RW
marnie@bramwelloakes.co.uk
www.bramwelloakes.co.uk
Please use attached logo - I require the business card and company stationery - cutting edge design please

```html
<!DOCTYPE html>
<html lang="en">
<head>
<meta charset="utf-8">
<title>Bramwell Oakes Recruitment – Business Card</title>
<link rel="stylesheet" href="https://fonts.googleapis.com/css2?family=Cinzel:wght@400;600&display=swap">
<style>
  :root {
    --page: #ecebe8;
    --card: #ffffff;
    --navy: #27246e;
    --navy-deep: #1c1a55;
    --navy-light: #3a37a0;
    --rule: #c9c9d6;
    --ink-light: #ffffff;
  }
  html, body {
    margin: 0;
    width: 1200px;
    height: 902px;
    overflow: hidden;
    background: var(--page);
  }
  .card {
    position: absolute;
    left: 110px;
    top: 166px;
    width: 980px;
    height: 570px;
    background: var(--card);
    box-shadow: 0 10px 30px rgba(0,0,0,0.18);
    font-family: "Cinzel", "Times New Roman", serif;
    overflow: hidden;
  }
  .brand {
    position: absolute;
    left: 62px;
    top: 62px;
    display: flex;
    align-items: center;
    gap: 26px;
  }
  .brand-mark {
    width: 112px;
    height: 112px;
    background: var(--navy);
  }
  .brand-name {
    color: var(--navy);
    font-weight: 400;
    font-size: 44px;
    line-height: 1.02;
    letter-spacing: 1px;
  }
  .brand-name .sub {
    display: block;
    font-size: 28px;
    letter-spacing: 6px;
    margin-top: 6px;
    padding-top: 6px;
    border-top: 1px solid var(--rule);
  }
  .band {
    position: absolute;
    left: 0;
    top: 286px;
    width: 100%;
    height: 204px;
    background: linear-gradient(180deg, var(--navy-light) 0%, var(--navy) 14%, var(--navy-deep) 100%);
    border-top: 3px solid #d8d8e4;
    color: var(--ink-light);
  }
  .holder {
    position: absolute;
    right: 44px;
    top: 28px;
    text-align: right;
    letter-spacing: 2px;
  }
  .holder-name { font-size: 22px; }
  .holder-role { font-size: 16px; margin-top: 4px; }
  .contacts {
    list-style: none;
    margin: 0;
    padding: 0;
    position: absolute;
    left: 30px;
    top: 24px;
    font-size: 13.5px;
    line-height: 22px;
    letter-spacing: 1.2px;
  }
  .contacts li { display: flex; align-items: center; gap: 10px; }
  .contacts .indent { padding-left: 22px; }
  .contacts svg { width: 12px; height: 12px; flex: none; }
</style>
</head>
<body>
  <div class="card">
    <div class="brand">
      <div class="brand-mark"></div>
      <div class="brand-name">Bramwell<br>Oakes<span class="sub">Recruitment</span></div>
    </div>

    <div class="band">
      <ul class="contacts">
        <li><svg viewBox="0 0 12 12"><circle cx="6" cy="6" r="5.5" fill="#fff"/><path d="M6 2.5a2 2 0 0 0-2 2c0 1.6 2 4.5 2 4.5s2-2.9 2-4.5a2 2 0 0 0-2-2z" fill="#27246e"/></svg>42 Quillmere Road Teddington</li>
        <li class="indent">Middlesex KT4 9RW</li>
        <li><svg viewBox="0 0 12 12"><circle cx="6" cy="6" r="5.5" fill="#fff"/><path d="M4 3l1.2 1.4-.6.8a4 4 0 0 0 2.2 2.2l.8-.6L9 8l-.8 1A5 5 0 0 1 3 3.8z" fill="#27246e"/></svg>0330 5550 174</li>
        <li><svg viewBox="0 0 12 12"><circle cx="6" cy="6" r="5.5" fill="#fff"/><rect x="4.3" y="2.8" width="3.4" height="6.4" rx="0.6" fill="#27246e"/></svg>07700 900316</li>
        <li><svg viewBox="0 0 12 12"><circle cx="6" cy="6" r="5.5" fill="#fff"/><rect x="3.2" y="4" width="5.6" height="4" fill="#27246e"/></svg>0330 5550 175</li>
        <li><svg viewBox="0 0 12 12"><circle cx="6" cy="6" r="5.5" fill="#fff"/><path d="M3 4h6v4H3z M3 4l3 2.2L9 4" fill="none" stroke="#27246e" stroke-width="1"/></svg>marnie@bramwelloakes.co.uk</li>
        <li><svg viewBox="0 0 12 12"><circle cx="6" cy="6" r="5.5" fill="#fff"/><circle cx="6" cy="6" r="3" fill="none" stroke="#27246e" stroke-width="1"/><path d="M3 6h6M6 3v6" stroke="#27246e" stroke-width="0.8"/></svg>www.bramwelloakes.co.uk</li>
      </ul>
      <div class="holder">
        <div class="holder-name">Marnie Thwaite</div>
        <div class="holder-role">Director</div>
      </div>
    </div>
  </div>
</body>
</html>
```